NEW Wordpress Website Design for a Dynamic Long Term Healthcare Company in Hawaii

I would like a new website design for my current company, Marlowe Kin Partners, which has two different brands - Marlowe Homecare and Marlowe Senior Living. You can see the current website at www.marlowekin.example. The website should be built using Wordpress Software and the Elementor theme. The website should have a local Hawaii island/tropical feel, but look professional for healthcare. I'm looking for something fresh, and want the designer to select colors, styles, etc.

In the Header, on all pages, I would like a menu that includes Home Care, Senior Living, Rates, and About Us.
Under each of the Header Menu Titles, I would like these drop downs included:
Home Care (drop down pages)- Nurse Aide Care, 24-Hour Home Care, Skilled Nursing, Lifestyle Aide, Hospice at Home, Bathing & Meal Service.
Senior Living (drop down pages) - Long-Term Stay, Short-Term Stay.
Rates (drop down page) - Rates.
About Us (drop down pages) - Our Mission, Porch Chats, About Dana Marlowe.

In the footer, on all pages, you should include the address: 238 Pueo Ridge Rd, Suite 120, Honolulu, HI 96822. Phone number: 808-555-0173
The footer should also include buttons for a page called Learn, Caregiver Jobs, and each of the service page links to include: Nurse Aide Care, 24-Hour Home Care, Skilled Nursing, Lifestyle Aide, Hospice at Home, Bathing & Meal Service.
Please don't take the current website and redesign a few aspects. I'm looking for a completely different look and feel.

Target Market(s)

40-80 year olds

Industry/Entity Type

Long Term Healthcare

Coding

Coded - Design and coding required

Requirements
Should not have
• Our existing website as a template. We are looking for a complete redesign. Thank you.

```html
<!DOCTYPE html>
<html lang="en">
<head>
<meta charset="utf-8">
<title>Marlowe Kin Partners — Homecare &amp; Senior Living</title>
<link rel="stylesheet" href="https://fonts.googleapis.com/css2?family=Playfair+Display:wght@400;600;700&family=Lora:wght@400;600&display=swap">
<style>
:root{
  --coral:#e9776c;
  --coral-soft:#f3b3aa;
  --ink:#1f1f1f;
  --night:#1d1c1c;
  --text:#4a4a4a;
  --muted:#8a8a8a;
  --white:#ffffff;
}
*{box-sizing:border-box;margin:0;padding:0}
html,body{width:1200px;height:5004px;overflow:hidden}
body{position:relative;background:var(--white);font-family:"Lora",Georgia,serif;color:var(--text)}
.abs{position:absolute}
.btn{display:inline-block;background:var(--coral);color:var(--white);font-family:"Lora",Georgia,serif;font-size:15px;padding:9px 24px;border-radius:22px}
.eyebrow{font-size:15px;letter-spacing:2px;color:var(--coral);text-transform:uppercase}
h1,h2,h3{font-family:"Playfair Display",Georgia,serif;font-weight:400;color:var(--ink)}

/* top bar */
.topbar{position:absolute;left:0;top:0;width:1200px;height:32px;background:var(--coral)}
.topbar .mail{position:absolute;right:210px;top:7px;color:#fff;font-size:13px;display:flex;gap:6px;align-items:center}
.topbar .phone{position:absolute;right:60px;top:4px;background:#fff;color:var(--coral);font-size:13px;padding:3px 14px;border-radius:12px;display:flex;gap:6px;align-items:center}

/* header */
.site-header{position:absolute;left:0;top:32px;width:1200px;height:128px;background:#fff}
.brand{position:absolute;left:60px;top:30px;display:flex;align-items:center;gap:12px}
.brand .dot{width:16px;height:16px;border-radius:50%;background:var(--coral)}
.brand .name{font-family:"Playfair Display",Georgia,serif;font-size:38px;color:var(--coral)}
.menu{position:absolute;left:540px;top:48px;display:flex;gap:40px;font-size:15px;color:var(--ink)}
.menu span::after{content:" ▾";font-size:10px;color:var(--coral)}
.site-header .btn{position:absolute;right:68px;top:40px;padding:9px 22px;font-size:14px}

/* hero */
.hero{position:absolute;left:0;top:160px;width:1200px;height:520px}
.hero-photo{position:absolute;inset:0;background:linear-gradient(90deg,rgba(40,20,15,.85) 0%,rgba(60,35,25,.55) 40%,rgba(150,110,80,.2) 75%),linear-gradient(180deg,#a7866b,#6a4a3a 60%,#c7a584)}
.hero .kicker{position:absolute;left:60px;top:92px;color:#fff;font-size:22px;font-family:"Playfair Display",Georgia,serif}
.hero h1{position:absolute;left:60px;top:122px;width:560px;color:#fff;font-size:54px;line-height:1.08;font-weight:700}
.hero h1 em{font-style:normal;color:var(--coral)}
.hero p{position:absolute;left:60px;top:252px;width:470px;color:#fff;font-size:15px;line-height:1.55}
.hero .btn{position:absolute;left:60px;top:352px}
.hero-edge{position:absolute;left:0;top:380px}

/* photo panels */
.photo-panel{position:absolute;width:520px;height:400px;border-radius:26px;border:6px solid #fff;box-shadow:0 0 0 4px var(--coral)}

/* about */
.about .text{position:absolute;left:650px;top:930px;width:480px}
.about h2{font-size:42px;line-height:1.2;margin:10px 0 26px}
.about p{font-size:15px;line-height:1.6}
.about .btn{margin-top:40px}

/* feature cards */
.feature{position:absolute;top:1488px;width:530px;height:440px;border-radius:12px;overflow:hidden;color:#fff}
.feature .bg{position:absolute;inset:0}
.feature.left{left:60px}
.feature.left .bg{background:linear-gradient(180deg,rgba(120,40,35,.78),rgba(80,25,22,.9)),linear-gradient(135deg,#b07a68,#5a3a32)}
.feature.right{left:610px}
.feature.right .bg{background:linear-gradient(180deg,rgba(30,30,30,.8),rgba(20,20,20,.92)),linear-gradient(135deg,#7a6a5e,#3a3330)}
.feature h3{position:absolute;left:36px;top:48px;width:440px;color:#fff;font-size:40px;line-height:1.15}
.feature p{position:absolute;left:36px;top:168px;width:440px;font-size:14px;line-height:1.55}
.feature .btn{position:absolute;left:36px;top:300px;font-size:14px;padding:8px 20px}

/* overview */
.overview .text{position:absolute;left:60px;top:2040px;width:480px}
.overview h2{font-size:44px;line-height:1.12;margin-bottom:22px}
.overview p{font-size:14.5px;line-height:1.6}
.overview .btn{margin-top:22px}

/* pillars */
.pillars{position:absolute;left:0;top:2420px;width:1200px;height:1060px}
.pillars .head{position:absolute;left:0;top:88px;width:1200px;text-align:center}
.pillars .head .eyebrow{color:#fff;font-size:14px}
.pillars .head h2{color:#fff;font-size:44px;margin-top:8px}
.pillar{position:absolute;top:2620px;width:258px;height:372px;background:#fff;border-radius:14px;overflow:hidden}
.pillar .photo{position:absolute;left:0;width:258px;height:186px}
.pillar .body{position:absolute;left:0;width:258px;height:186px;padding:20px}
.pillar h3{font-size:22px;margin-bottom:10px}
.pillar p{font-size:12.5px;line-height:1.5;color:var(--text)}
.pillar .more{font-size:11px;color:var(--coral);margin-top:8px;letter-spacing:1px}
.pillar .badge{position:absolute;left:105px;width:48px;height:48px;border-radius:50%;background:var(--coral);border:4px solid #fff;display:flex;align-items:center;justify-content:center}
.choice{position:absolute;left:68px;top:3072px;width:1064px;height:308px;background:var(--coral);border-radius:14px;text-align:center;color:#fff}
.choice .eyebrow{color:#fff;font-size:14px;margin-top:34px;display:block}
.choice h2{color:#fff;font-size:42px;margin-top:4px}
.choice p{width:840px;margin:16px auto 0;font-size:14px;line-height:1.55}
.choice .btn-light{display:inline-block;margin-top:24px;background:#fff;color:var(--ink);font-size:14px;padding:8px 24px;border-radius:20px}

/* senior living */
.senior .text{position:absolute;left:650px;top:3520px;width:480px}
.senior h2{font-size:46px;line-height:1.1}
.senior h2 span{display:block}
.senior p{margin-top:24px;font-size:14.5px;line-height:1.6}
.senior .btn{margin-top:40px}

/* consultation */
.consult{position:absolute;left:0;top:3940px;width:1200px;height:660px}
.consult h2{position:absolute;left:0;top:108px;width:1200px;text-align:center;color:#fff;font-size:46px;line-height:1.15}
.form{position:absolute;left:188px;top:4180px;width:824px;height:160px}
.field{position:absolute;height:44px;background:#fff;font-size:12.5px;color:var(--muted);padding:13px 14px;white-space:nowrap}
.field.select{padding-right:28px}
.field.select::after{content:"▾";position:absolute;right:12px;top:12px;color:var(--muted)}
.consent{position:absolute;left:0;top:4356px;width:1200px;text-align:center;color:#fff;font-size:11px}
.submit{position:absolute;left:500px;top:4384px;width:200px;height:40px;background:var(--night);color:#fff;font-size:14px;letter-spacing:1px;text-align:center;line-height:40px;border-radius:20px}

/* footer */
.site-footer{position:absolute;left:0;top:4560px;width:1200px;height:444px;background:var(--night)}
.site-footer .brand{top:70px}
.site-footer .brand .name{color:#fff}
.site-footer .tag{position:absolute;left:60px;top:140px;width:310px;color:#cfcfcf;font-size:13px;line-height:1.55}
.site-footer .actions{position:absolute;left:60px;top:218px;display:flex;gap:12px}
.site-footer .actions .alt{background:#fff;color:var(--ink)}
.col{position:absolute;top:54px}
.col h4{font-family:"Playfair Display",Georgia,serif;font-weight:400;color:var(--coral);font-size:20px;margin-bottom:18px}
.col li{list-style:none;color:#d8d8d8;font-size:13px;line-height:2}
.col .row{display:flex;gap:10px;align-items:flex-start;color:#d8d8d8;font-size:13px;line-height:1.5;margin-bottom:14px}
.col .ico{flex:none;width:22px;height:22px;border-radius:50%;background:var(--coral);display:flex;align-items:center;justify-content:center}
.bottom-bar{position:absolute;left:0;top:392px;width:1200px;height:52px;border-top:1px solid #3a3939}
.bottom-bar .copy{position:absolute;left:60px;top:18px;color:#bdbdbd;font-size:12px}
.bottom-bar .copy b{color:var(--coral);font-weight:400}
.bottom-bar .dots{position:absolute;right:60px;top:18px;display:flex;gap:12px}
.bottom-bar .dots i{width:14px;height:14px;border-radius:50%;background:var(--coral);display:block}
</style>
</head>
<body>

<!-- top bar -->
<div class="topbar">
  <div class="mail"><svg width="14" height="10" viewBox="0 0 14 10"><rect x=".5" y=".5" width="13" height="9" fill="none" stroke="#fff"/><path d="M.5 .5 7 6 13.5 .5" fill="none" stroke="#fff"/></svg>info@marlowekin.example</div>
  <div class="phone"><svg width="12" height="12" viewBox="0 0 24 24"><path fill="#e9776c" d="M6.6 10.8a15 15 0 0 0 6.6 6.6l2.2-2.2a1 1 0 0 1 1-.25 11.4 11.4 0 0 0 3.6.57 1 1 0 0 1 1 1V20a1 1 0 0 1-1 1A17 17 0 0 1 3 4a1 1 0 0 1 1-1h3.5a1 1 0 0 1 1 1c0 1.250.2 2.450.57 3.57a1 1 0 0 1-.25 1z"/></svg>808-555-0173</div>
</div>

<!-- header -->
<header class="site-header">
  <div class="brand"><i class="dot"></i><span class="name">Marlowe</span></div>
  <nav class="menu"><span>Home Care</span><span>Senior Living</span><span>Rates</span><span>About Us</span></nav>
  <a class="btn">Contact Us</a>
</header>

<!-- hero -->
<section class="hero">
  <div class="hero-photo" role="img" aria-label="Caregiver helping an older man stand up in a warm living room"></div>
  <div class="kicker">Home Care</div>
  <h1>Marlowe Homecare Services <em>Offered</em></h1>
  <p>Homecare services are a range of medical, personal, and supportive care services provided in an individual's own home.</p>
  <a class="btn">View Offer</a>
  <svg class="hero-edge" width="1200" height="160" viewBox="0 0 1200 160">
    <path d="M0,60 C260,60 470,70 560,110 C585,122 595,134 600,140 C605,134 615,122 640,110 C730,70 940,60 1200,60 L1200,160 L0,160 Z" fill="#fff"/>
    <path d="M0,60 C260,60 470,70 560,110 C585,122 595,134 600,140 C605,134 615,122 640,110 C730,70 940,60 1200,60" fill="none" stroke="#e9776c" stroke-width="8"/>
  </svg>
</section>

<!-- about -->
<section class="about">
  <div class="photo-panel" style="left:60px;top:856px;background:linear-gradient(135deg,#b9c98e,#6f8a5a)" role="img" aria-label="Two smiling women sitting together on a sofa"></div>
  <div class="text">
    <div class="eyebrow">About Us</div>
    <h2>Marlowe Home Care Group</h2>
    <p>At Marlowe Kin Partners, our mission is to provide compassionate and professional long-term healthcare services that empower individuals to maintain their highest level of independence, health, and wellbeing in the comfort of their own homes or ours, either through our licensed home healthcare agency...</p>
    <a class="btn">Read More</a>
  </div>
</section>

<!-- feature cards -->
<article class="feature left">
  <div class="bg" role="img" aria-label="Caregiver assisting an elderly client at home"></div>
  <h3>Professional Care In Your Home</h3>
  <p>Marlowe Homecare understands that every person's care journey is unique. We tailor our in-home services to meet the diverse nursing experience of professional quality care and safety within the comfort and convenience of your own home.</p>
  <a class="btn">Schedule Care Assessment</a>
</article>
<article class="feature right">
  <div class="bg" role="img" aria-label="Residents relaxing in a senior living home"></div>
  <h3>Trusted Care In Our Home</h3>
  <p>Marlowe Senior Living creates a warm, supportive, and enriching care home environment where seniors can thrive in their golden years. We provide residential care that promotes wellbeing, connection, and dignity of each individual.</p>
  <a class="btn">Schedule Tour</a>
</article>

<!-- overview -->
<section class="overview">
  <div class="text">
    <h2>Homecare<br>Services Overview</h2>
    <p>Marlowe Homecare is a leading provider of compassionate and professional homecare services. With a deep commitment to enhancing the quality of life for individuals of all ages, our company is dedicated to delivering personalized care to the comfort of our clients' homes.</p>
    <a class="btn">Read More</a>
  </div>
  <div class="photo-panel" style="left:620px;top:1956px;background:linear-gradient(135deg,#d7b690,#8f6e52)" role="img" aria-label="Caregivers serving seniors at a dining table"></div>
</section>

<!-- pillars -->
<section class="pillars">
  <svg class="abs" style="left:0;top:0" width="1200" height="1060" viewBox="0 0 1200 1060">
    <path d="M0,0 H1200 V990 C940,990 730,1000 640,1040 C615,1050 605,1056 600,1060 C595,1056 585,1050 560,1040 C470,1000 260,990 0,990 Z" fill="#1d1c1c"/>
    <path d="M0,990 C260,990 470,1000 560,1040 C585,1050 595,1056 600,1060 C605,1056 615,1050 640,1040 C730,1000 940,990 1200,990" fill="none" stroke="#e9776c" stroke-width="6"/>
  </svg>
  <div class="head">
    <div class="eyebrow">Services</div>
    <h2>Key Pillars of Our Mission</h2>
  </div>
</section>

<article class="pillar" style="left:68px">
  <div class="photo" style="top:0;background:linear-gradient(135deg,#d9c3b0,#8c7466)" role="img" aria-label="Smiling senior woman with a nurse aide"></div>
  <div class="badge" style="top:162px"><svg width="20" height="20" viewBox="0 0 24 24"><path fill="#fff" d="M12 21s-8-5.3-8-11a4.5 4.5 0 0 1 8-2.8A4.5 4.5 0 0 1 20 10c0 5.7-8 11-8 11z"/></svg></div>
  <div class="body" style="top:186px;padding-top:30px">
    <h3>Nurse Aide Care</h3>
    <p>Duis aute irure dolor in reprehenderit in voluptate with our ciillum dolore eu fugiat nulla</p>
    <div class="more">READ MORE</div>
  </div>
</article>
<article class="pillar" style="left:338px">
  <div class="body" style="top:0">
    <h3>24-Hour Home Care</h3>
    <p>Duis aute irure dolor in reprehenderit in voluptate with our ciillum dolore eu fugiat nulla</p>
    <div class="more">READ MORE</div>
  </div>
  <div class="photo" style="top:186px;background:linear-gradient(135deg,#c9d7a8,#6f8d5e)" role="img" aria-label="Caregiver walking with a senior outdoors"></div>
  <div class="badge" style="top:162px"><svg width="20" height="20" viewBox="0 0 24 24"><circle cx="12" cy="12" r="8" fill="none" stroke="#fff" stroke-width="2"/><path d="M12 7v5l3 2" fill="none" stroke="#fff" stroke-width="2"/></svg></div>
</article>
<article class="pillar" style="left:608px">
  <div class="photo" style="top:0;background:linear-gradient(135deg,#c8d3dd,#6f7f92)" role="img" aria-label="Nurse checking on a senior patient"></div>
  <div class="badge" style="top:162px"><svg width="20" height="20" viewBox="0 0 24 24"><path fill="#fff" d="M10 4h4v6h6v4h-6v6h-4v-6H4v-4h6z"/></svg></div>
  <div class="body" style="top:186px;padding-top:30px">
    <h3>Skilled Nursing</h3>
    <p>Duis aute irure dolor in reprehenderit in voluptate with our ciillum dolore eu fugiat nulla</p>
    <div class="more">READ MORE</div>
  </div>
</article>
<article class="pillar" style="left:878px">
  <div class="body" style="top:0">
    <h3>Lifestyle Aide</h3>
    <p>Duis aute irure dolor in reprehenderit in voluptate with our ciillum dolore eu fugiat nulla</p>
    <div class="more">READ MORE</div>
  </div>
  <div class="photo" style="top:186px;background:linear-gradient(135deg,#e3cdb8,#a08064)" role="img" aria-label="Seniors enjoying an activity together"></div>
  <div class="badge" style="top:162px"><svg width="20" height="20" viewBox="0 0 24 24"><circle cx="12" cy="8" r="4" fill="#fff"/><path fill="#fff" d="M4 21a8 8 0 0 1 16 0z"/></svg></div>
</article>

<section class="choice">
  <span class="eyebrow">Hawaii's Choice</span>
  <h2>Homecare &amp; Senior Living</h2>
  <p>Marlowe Homecare provides a variety of professional in-home health care services throughout the entire island of Oahu. Marlowe Senior Living, a beautiful adult Residential Care Home, is located on the windward side of Oahu in Kailua.</p>
  <a class="btn-light">Show Info</a>
</section>

<!-- senior living -->
<section class="senior">
  <div class="photo-panel" style="left:60px;top:3476px;background:linear-gradient(135deg,#e6c9a6,#9d7a5e)" role="img" aria-label="Three senior women laughing together on a couch"></div>
  <div class="text">
    <h2><span>Marlowe</span><span>Senior Living</span></h2>
    <p>Choosing a senior living facility is crucial because it directly impacts the quality of life, well-being, and safety of seniors as they age. Marlowe Senior Living offers a structured and supportive environment that addresses the unique needs and challenges that come with aging.</p>
    <a class="btn">Read More</a>
  </div>
</section>

<!-- consultation -->
<section class="consult">
  <svg class="abs" style="left:0;top:0" width="1200" height="660" viewBox="0 0 1200 660">
    <path d="M0,40 C200,10 420,0 540,30 C575,40 592,52 600,64 C608,52 625,40 660,30 C780,0 1000,10 1200,40 V560 C940,560 730,570 640,610 C615,620 605,626 600,632 C595,626 585,620 560,610 C470,570 260,560 0,560 Z" fill="#e9776c"/>
    <path d="M0,40 C200,10 420,0 540,30 C575,40 592,52 600,64 C608,52 625,40 660,30 C780,0 1000,10 1200,40" fill="none" stroke="#f3b3aa" stroke-width="5"/>
  </svg>
  <h2>Schedule a<br>Complimentary Care Consultation</h2>
</section>

<form class="form">
  <div class="field" style="left:0;top:0;width:266px">Name</div>
  <div class="field" style="left:279px;top:0;width:266px">Email</div>
  <div class="field" style="left:558px;top:0;width:266px">Phone</div>
  <div class="field select" style="left:0;top:58px;width:402px">How Can We Help?</div>
  <div class="field" style="left:422px;top:58px;width:402px;height:102px">Questions / Comments</div>
  <div class="field select" style="left:0;top:116px;width:210px">How did you hear about us?</div>
  <div class="field" style="left:220px;top:116px;width:182px">Best time to reach you?</div>
</form>
<p class="consent">You agree to receive phone calls and text messages from our team to assist you.</p>
<div class="submit">SUBMIT</div>

<!-- footer -->
<footer class="site-footer">
  <div class="brand"><i class="dot"></i><span class="name">Marlowe</span></div>
  <p class="tag">Caregiving is a series of small acts of care that alter the course of someone's life.</p>
  <div class="actions"><a class="btn">Learn More</a><a class="btn alt">Caregiver Jobs</a></div>

  <div class="col" style="left:520px;width:210px">
    <h4>Contact Us</h4>
    <div class="row"><span class="ico"><svg width="10" height="12" viewBox="0 0 24 28"><path fill="#fff" d="M12 0a10 10 0 0 0-10 10c0 7.5 10 18 10 18s10-10.5 10-18A10 10 0 0 0 12 0zm0 14a4 4 0 1 1 0-8 4 4 0 0 1 0 8z"/></svg></span>238 Pueo Ridge Rd, Suite 120, Honolulu, HI 96822</div>
    <div class="row"><span class="ico"><svg width="11" height="11" viewBox="0 0 24 24"><path fill="#fff" d="M6.6 10.8a15 15 0 0 0 6.6 6.6l2.2-2.2a1 1 0 0 1 1-.25 11.4 11.4 0 0 0 3.6.57 1 1 0 0 1 1 1V20a1 1 0 0 1-1 1A17 17 0 0 1 3 4a1 1 0 0 1 1-1h3.5a1 1 0 0 1 1 1c0 1.25.2 2.45.57 3.57a1 1 0 0 1-.25 1z"/></svg></span>808-555-0173</div>
    <div class="row"><span class="ico"><svg width="11" height="8" viewBox="0 0 14 10"><rect x=".5" y=".5" width="13" height="9" fill="none" stroke="#fff"/><path d="M.5 .5 7 6 13.5 .5" fill="none" stroke="#fff"/></svg></span>info@marlowekin.example</div>
  </div>
  <div class="col" style="left:780px">
    <h4>Quick Links</h4>
    <ul><li>Home Care</li><li>Senior Living</li><li>Rates</li><li>About Us</li><li>Contact Us</li></ul>
  </div>
  <div class="col" style="left:960px">
    <h4>Services</h4>
    <ul><li>Nurse Aide Care</li><li>24-Hour Home Care</li><li>Skilled Nursing</li><li>Lifestyle Aide</li><li>Hospice at Home</li><li>Bathing &amp; Meal Service</li></ul>
  </div>

  <div class="bottom-bar">
    <div class="copy">© <b>Marlowe Kin Partners</b>, 2024. All Rights Reserved</div>
    <div class="dots"><i></i><i></i><i></i></div>
  </div>
</footer>

</body>
</html>
```